Real Estate Company needs Stationary.
Business Cards, Letterhead, Envelope Stationary etc...
Real Estate Company needs Stationary. -
Creative Brief
Professional
Tomas Velbrik
Broker
3871 W. Marrowfield Ave., Suite K-214 Marrowfield TX, 75318
1 (866) 514-VKOR (5867)
tomas@vkorhomesllc.example
www.vkorhomesllc.example
We are a real estate company looking for a slick contemporary design. Use logo in the design. Use logo colors if desired. Would like Business cards, Letterhead, and Envelope. I would like all the stationary items to carry the same theme my logo protrays. Email me with questions.
I would like the logo on back, and open to any other sugestions.

```html
<!DOCTYPE html>
<html lang="en">
<head>
<meta charset="utf-8">
<title>vKorHomes Stationery</title>
<link href="https://fonts.googleapis.com/css2?family=Open+Sans:wght@400;600;700&display=swap" rel="stylesheet">
<style>
:root{
  --backdrop:#8a4a22;
  --paper:#ffffff;
  --silver-light:#f2f2f2;
  --silver-dark:#b9bcbf;
  --brand-blue:#1f73c9;
  --brand-blue-deep:#0d4f9e;
  --brand-green:#59b33b;
  --ink:#3b3f44;
  --ink-soft:#7b8087;
}
*{box-sizing:border-box;margin:0;padding:0}
html,body{width:1200px;height:545px;overflow:hidden}
body{background:var(--backdrop);font-family:"Open Sans",Arial,sans-serif;color:var(--ink);position:relative}
.piece{position:absolute;background:var(--paper);overflow:hidden;box-shadow:0 2px 6px rgba(0,0,0,.35)}
.swoosh{position:absolute;left:0;width:100%;display:block}
.swoosh.top{top:0}
.swoosh.bottom{bottom:0}
.brand{position:absolute;display:flex;align-items:center;gap:4px;font-weight:700;color:var(--brand-blue-deep);white-space:nowrap;z-index:2}
.brand .mark{display:inline-block;background:var(--brand-green)}
.tiny{position:absolute;font-size:4px;line-height:1.45;color:var(--ink)}
.small{position:absolute;font-size:5px;line-height:1.5;color:var(--ink)}

/* business cards */
.card{width:106px;height:56px}
.card-front-a{left:86px;top:72px}
.card-front-b{left:202px;top:72px}
.card-back-a{left:86px;top:144px}
.card-back-b{left:202px;top:144px}
.card .brand{font-size:7px}
.card .brand .mark{width:6px;height:6px}

/* envelope */
.envelope-back{left:30px;top:222px;width:262px;height:92px;background:#f4f4f4}
.envelope-flap{position:absolute;inset:0}
.envelope-front{left:66px;top:264px;width:258px;height:120px;z-index:3}
.envelope-front .brand{font-size:12px;right:14px;top:4px}
.envelope-front .brand .mark{width:10px;height:10px}

/* letterhead */
.letterhead{left:336px;top:58px;width:266px;height:424px}
.letterhead .brand{font-size:13px;right:18px;top:12px}
.letterhead .brand .mark{width:11px;height:11px}
.faint-circle{position:absolute;border-radius:50%;background:var(--brand-blue);opacity:.08}
.letterhead .faint-circle{width:110px;height:110px;left:78px;top:170px}
.letterhead .footer-line{position:absolute;left:12px;right:12px;bottom:8px;font-size:4px;color:var(--ink-soft);text-align:center;white-space:nowrap;z-index:2}

/* presentation folder */
.folder-inside{left:628px;top:46px;width:262px;height:484px;background:linear-gradient(160deg,#2f8ee6 0%,var(--brand-blue) 45%,var(--brand-blue-deep) 100%)}
.folder-inside .faint-circle{width:120px;height:120px;left:60px;top:80px;background:#fff;opacity:.12}
.folder-inside .brand{left:80px;top:70px;font-size:12px;color:#cfe3f7}
.folder-inside .brand .mark{width:10px;height:10px;background:#cfe3f7}
.folder-inside .contact{position:absolute;left:22px;top:250px;font-size:5px;line-height:1.55;color:#e6f0fb}
.pocket{position:absolute;left:0;bottom:0;width:100%;height:160px}
.folder-cover{left:890px;top:46px;width:240px;height:436px}
.folder-cover .brand{font-size:14px;left:28px;top:10px}
.folder-cover .brand .mark{width:12px;height:12px}
.folder-cover .faint-circle{width:130px;height:130px;left:70px;top:110px}
</style>
</head>
<body>

<div class="piece card card-front-a">
  <svg class="swoosh top" viewBox="0 0 100 30" preserveAspectRatio="none" height="14">
    <defs><linearGradient id="sv" x1="0" y1="0" x2="0" y2="1"><stop offset="0" stop-color="#f2f2f2"/><stop offset="1" stop-color="#b9bcbf"/></linearGradient></defs>
    <path d="M0 0H100V16C70 6 40 26 0 12Z" fill="url(#sv)"/>
    <path d="M0 12C40 26 70 6 100 16V20C70 10 40 30 0 16Z" fill="#1f73c9"/>
    <path d="M0 17C40 30 70 12 100 21V22C70 14 40 32 0 18Z" fill="#59b33b"/>
  </svg>
  <div class="brand" style="right:8px;top:15px"><span class="mark"></span>vKorHomes</div>
  <div class="tiny" style="left:8px;top:27px"><b>Tomas Velbrik</b><br>Broker<br>1 (866) 514-VKOR (5867)<br>tomas@vkorhomesllc.example</div>
</div>

<div class="piece card card-front-b">
  <svg class="swoosh top" viewBox="0 0 100 30" preserveAspectRatio="none" height="14">
    <path d="M0 0H100V16C70 6 40 26 0 12Z" fill="url(#sv)"/>
    <path d="M0 12C40 26 70 6 100 16V20C70 10 40 30 0 16Z" fill="#1f73c9"/>
    <path d="M0 17C40 30 70 12 100 21V22C70 14 40 32 0 18Z" fill="#59b33b"/>
  </svg>
  <div class="brand" style="right:8px;top:15px"><span class="mark"></span>vKorHomes</div>
  <div class="tiny" style="left:8px;top:27px">3871 W. Marrowfield Ave., Suite K-214<br>Marrowfield TX, 75318<br>www.vkorhomesllc.example</div>
</div>

<div class="piece card card-back-a">
  <svg class="swoosh bottom" viewBox="0 0 100 30" preserveAspectRatio="none" height="18">
    <path d="M0 14C40 2 70 24 100 10V30H0Z" fill="url(#sv)"/>
    <path d="M0 14C40 2 70 24 100 10V13C70 27 40 5 0 17Z" fill="#1f73c9"/>
  </svg>
  <div class="brand" style="left:24px;top:14px"><span class="mark"></span>vKorHomes</div>
</div>

<div class="piece card card-back-b">
  <svg class="swoosh bottom" viewBox="0 0 100 30" preserveAspectRatio="none" height="18">
    <path d="M0 14C40 2 70 24 100 10V30H0Z" fill="url(#sv)"/>
    <path d="M0 14C40 2 70 24 100 10V13C70 27 40 5 0 17Z" fill="#59b33b"/>
  </svg>
  <div class="tiny" style="left:10px;top:12px">Tomas Velbrik · Broker<br>1 (866) 514-VKOR (5867)<br>www.vkorhomesllc.example</div>
</div>

<div class="piece envelope-back">
  <svg class="envelope-flap" viewBox="0 0 262 92" preserveAspectRatio="none">
    <path d="M0 0H262L148 40Q131 46 114 40Z" fill="#e3e4e6"/>
    <path d="M0 0L114 40Q131 46 148 40L262 0" fill="none" stroke="#c9cbce" stroke-width="1"/>
  </svg>
</div>

<div class="piece envelope-front">
  <svg class="swoosh top" viewBox="0 0 100 30" preserveAspectRatio="none" height="44">
    <path d="M0 0H100V16C70 6 40 26 0 12Z" fill="url(#sv)"/>
    <path d="M0 12C40 26 70 6 100 16V20C70 10 40 30 0 16Z" fill="#1f73c9"/>
    <path d="M0 17C40 30 70 12 100 21V22C70 14 40 32 0 18Z" fill="#59b33b"/>
  </svg>
  <div class="brand"><span class="mark"></span>vKorHomes</div>
  <div class="small" style="left:14px;top:70px">3871 W. Marrowfield Ave., Suite K-214<br>Marrowfield TX, 75318<br>1 (866) 514-VKOR (5867)<br>tomas@vkorhomesllc.example<br>www.vkorhomesllc.example</div>
</div>

<div class="piece letterhead">
  <svg class="swoosh top" viewBox="0 0 100 30" preserveAspectRatio="none" height="82">
    <path d="M0 0H100V16C70 6 40 26 0 12Z" fill="url(#sv)"/>
    <path d="M0 12C40 26 70 6 100 16V20C70 10 40 30 0 16Z" fill="#1f73c9"/>
    <path d="M0 17C40 30 70 12 100 21V22C70 14 40 32 0 18Z" fill="#59b33b"/>
  </svg>
  <div class="brand"><span class="mark"></span>vKorHomes</div>
  <div class="faint-circle"></div>
  <svg class="swoosh bottom" viewBox="0 0 100 30" preserveAspectRatio="none" height="40">
    <path d="M0 16C40 4 70 24 100 12V30H0Z" fill="url(#sv)"/>
    <path d="M0 16C40 4 70 24 100 12V15C70 27 40 7 0 19Z" fill="#1f73c9"/>
  </svg>
  <div class="footer-line">3871 W. Marrowfield Ave., Suite K-214 Marrowfield TX, 75318 · 1 (866) 514-VKOR (5867) · tomas@vkorhomesllc.example</div>
</div>

<div class="piece folder-inside">
  <div class="faint-circle"></div>
  <div class="brand"><span class="mark"></span>vKorHomes</div>
  <div class="contact">Tomas Velbrik, Broker<br>3871 W. Marrowfield Ave., Suite K-214<br>Marrowfield TX, 75318<br>1 (866) 514-VKOR (5867)<br>tomas@vkorhomesllc.example<br>www.vkorhomesllc.example</div>
  <svg class="pocket" viewBox="0 0 262 160" preserveAspectRatio="none">
    <defs><linearGradient id="pk" x1="0" y1="0" x2="0" y2="1"><stop offset="0" stop-color="#2a86de"/><stop offset="1" stop-color="#0b4590"/></linearGradient></defs>
    <path d="M0 40Q130 0 262 20V160H0Z" fill="url(#pk)"/>
    <path d="M0 40Q130 0 262 20" fill="none" stroke="#6fb0ef" stroke-width="1"/>
    <path d="M90 110L104 100M110 124L118 118" stroke="#9cc9f4" stroke-width="1"/>
  </svg>
</div>

<div class="piece folder-cover">
  <svg class="swoosh top" viewBox="0 0 100 30" preserveAspectRatio="none" height="64">
    <path d="M0 0H100V18C70 8 40 24 0 14Z" fill="url(#sv)"/>
    <path d="M0 14C40 24 70 8 100 18V21C70 11 40 28 0 17Z" fill="#1f73c9"/>
  </svg>
  <div class="brand"><span class="mark"></span>vKorHomes</div>
  <div class="faint-circle"></div>
  <svg class="swoosh bottom" viewBox="0 0 100 60" preserveAspectRatio="none" height="150">
    <path d="M0 36C40 10 70 40 100 4V60H0Z" fill="url(#sv)"/>
    <path d="M0 36C40 10 70 40 100 4V14C70 46 40 18 0 42Z" fill="#1f73c9"/>
    <path d="M0 44C40 20 70 48 100 16V20C70 52 40 26 0 48Z" fill="#59b33b"/>
  </svg>
</div>

</body>
</html>
```